Web Page for Elearning project

SUMMARY OF REQUIREMENT
The requirement is to provide the graphic design for an eLearning project. I need the design elements for a main page layout which I can recreate in an eLearning authoring program (Quillet) using the graphic design you provide.

SUMMARY OF SITE PAGES
The web site has 11 sections with pages within each section. The user will navigate through all pages by clicking NEXT or by jumping to a page using either an index or table of contents (according to your design).

The sections are:
- Introduction
- DWT Cemeteries
- Fernhallow*
- Plain of Wrens (Catholic)*
- East Vales (Catholic)*
- Ashbury (Catholic)*
- Tallis Brook (Catholic)*
- Plain of Wrens (Presbyterian)*
- Pell Ridge*
- Summary
- Quiz

The sections with a "*" contain consistent pages - which I imagine could be accessed by clicking on a tab or button. I would need you to supply the graphics to be able to set them up in my elearning program. The pages are:
- History
- Map
- Contact
- Directions
- Services
- Sections

ONCE THE DESIGN IS ACCEPTED...
Ultimately I need the background graphics so I can implement the design in my elearning authoring program What else do you need to know?

SEE ATTACHED PDF FOR MORE DETAILS AND EXAMPLES OF WHAT I AM CURRENTLY WORKING WITH
Updates

Reason: Australia now has public holidays for the next 5 days.  Everyone back at work on 27-28 April.

Target Market(s)

The users are mostly middle-aged women who only have basic computer skills... needs to be easy to navigate.

Industry/Entity Type

Graphic Design

Requirements
Must have
• Light, fun but professional. Its training...should have a light/easy feel about it.

Must be easy to look at. The design should support the overall navigation/structure.
Nice to have
• easy to look at, light.
Should not have
• Should not use serif fonts.
I don't think we'd go for bold lime green or any really zany colours.

```html
<!DOCTYPE html>
<html lang="en">
<head>
<meta charset="utf-8">
<title>DWT Cemeteries Module – Fernhallow</title>
<link rel="stylesheet" href="https://fonts.googleapis.com/css2?family=Arimo:wght@400;700&family=Open+Sans:wght@400;600&display=swap">
<style>
  :root {
    --navy: #1d3f86;
    --crimson: #b3262b;
    --red-top: #c64a4c;
    --red-bottom: #a92f31;
    --shadow: #3a3a3a;
    --side-top: #a6cdf5;
    --side-bottom: #4a6fbf;
    --tab-top: #a8c9f0;
    --tab-bottom: #4f7cc9;
    --ink: #1a1a1a;
    --line: #b5b5b5;
    --muted: #8ea9c1;
    --white: #ffffff;
  }
  * { box-sizing: border-box; margin: 0; padding: 0; }
  html, body { width: 1200px; height: 891px; overflow: hidden; background: var(--white); }
  body { position: relative; font-family: "Arimo", Arial, sans-serif; color: var(--ink); }

  .brand { position: absolute; left: 48px; top: 70px; display: flex; align-items: center; gap: 12px; }
  .brand-dot { width: 22px; height: 22px; border-radius: 50%; background: var(--crimson); }
  .brand-name { font-family: "Arimo", Arial, sans-serif; font-weight: 700; font-size: 44px; color: var(--navy); letter-spacing: 2px; }

  .page-tab {
    position: absolute; left: 311px; top: 51px; width: 239px; height: 39px;
    background: linear-gradient(var(--tab-top), var(--tab-bottom));
    box-shadow: 4px 4px 0 var(--shadow);
    color: var(--white); font-size: 22px; line-height: 39px; padding-left: 15px;
  }

  .nav-btn {
    position: absolute; top: 47px; height: 46px;
    background: linear-gradient(var(--red-top), var(--red-bottom));
    box-shadow: 4px 4px 0 var(--shadow);
    color: var(--white); font-size: 26px; text-align: center; line-height: 46px;
  }
  .nav-btn.back { left: 859px; width: 127px; }
  .nav-btn.next { left: 1004px; width: 127px; }
  .nav-btn.close { left: 1149px; width: 44px; }

  .content {
    position: absolute; left: 311px; top: 113px; width: 885px; height: 584px;
    border: 1px solid var(--line); padding: 14px 14px;
    font-size: 16.4px; line-height: 26px;
  }
  .content p + p { margin-top: 26px; }

  .sections {
    position: absolute; left: 9px; top: 212px; width: 290px; height: 478px;
    background: linear-gradient(var(--side-top), var(--side-bottom));
    box-shadow: 5px 5px 0 var(--shadow);
    list-style: none; padding-top: 16px;
  }
  .sections li {
    display: flex; align-items: center; height: 41.4px; padding-left: 8px;
    font-family: "Open Sans", Verdana, sans-serif; font-size: 16.5px; color: #f3f6ff; letter-spacing: .3px;
  }
  .check { width: 20px; height: 20px; margin-right: 9px; background: #3f5f9c; border: 1px solid #d7e4f7; flex: none; }
  .check.done { background: #e9f2fb; }

  .utility { position: absolute; left: 12px; top: 714px; list-style: none; }
  .utility li { font-size: 16px; line-height: 23.5px; text-decoration: underline; }

  .topics { position: absolute; left: 396px; top: 724px; width: 745px; height: 92px; }
  .topic {
    position: absolute; top: 0; width: 98px; height: 88px;
    background: linear-gradient(var(--red-top), var(--red-bottom));
    box-shadow: 4px 4px 0 var(--shadow);
    color: var(--white); font-size: 16.5px; text-align: center;
  }
  .topic svg { position: absolute; left: 24px; top: 8px; width: 50px; height: 48px; }
  .topic span { position: absolute; left: 0; right: 0; bottom: 8px; }

  .module-mark { position: absolute; left: 14px; top: 848px; display: flex; align-items: center; gap: 14px; }
  .module-dot { width: 30px; height: 30px; border-radius: 50%; background: var(--muted); }
  .module-name { font-weight: 700; font-size: 22px; color: var(--muted); }

  .page-count { position: absolute; right: 15px; top: 848px; font-size: 21px; color: #2a2a2a; }
</style>
</head>
<body>
  <div class="brand"><span class="brand-dot"></span><span class="brand-name">DWT</span></div>

  <div class="page-tab">Fernhallow</div>
  <div class="nav-btn back">Back</div>
  <div class="nav-btn next">Next</div>
  <div class="nav-btn close">X</div>

  <main class="content">
    <p>Lorem ipsum dolor sit amet, consectetur adipiscing elit. Phasellus vitae nunc ut dolor sollicitudin lobortis. Maecenas elementum, enim ac convallis vulputate, leo neque suscipit magna, volutpat tristique nunc libero ac sapien. Vestibulum semper tortor sed enim accumsan tincidunt. Phasellus justo urna, ultricies et sagittis ac, porttitor consectetur diam. Fusce lacinia sapien a odio rhoncus elementum. In hac habitasse platea dictumst. Pellentesque ac mattis lacus. Aenean ultrices congue tortor, ullamcorper fermentum ligula tempor et. Suspendisse volutpat volutpat scelerisque. Praesent interdum lobortis erat, non accumsan ipsum elementum vel.</p>
    <p>Nam mattis vestibulum sollicitudin. Morbi a purus lorem. Duis vitae sapien posuere elit malesuada rhoncus. Suspendisse semper ligula sit amet mauris consectetur vel ultrices lectus ullamcorper. Ut risus sem, tristique in dapibus quis, porta ut lectus. Nullam egestas tellus vel metus dapibus gravida. Curabitur id lacus tortor. Fusce molestie fermentum tincidunt. Maecenas eget urna purus. Vivamus fringilla, tellus sed mollis varius, justo sem porta tellus, nec dictum enim purus non augue. Nullam ut libero velit, at tempus sapien. Fusce et diam mauris. Sed sit amet sapien pellentesque dolor mattis luctus. In hac habitasse platea dictumst. Etiam in sem lectus, non vehicula felis.</p>
  </main>

  <ul class="sections">
    <li><span class="check"></span>Introduction</li>
    <li><span class="check"></span>DWT Cemeteries</li>
    <li><svg class="check done" viewBox="0 0 20 20"><path d="M4 10 L8 14 L16 5" fill="none" stroke="#2f8fd8" stroke-width="2.5"/></svg>Fernhallow</li>
    <li><span class="check"></span>Plain of Wrens (Catholic)</li>
    <li><span class="check"></span>East Vales (Catholic)</li>
    <li><span class="check"></span>Ashbury (Catholic)</li>
    <li><span class="check"></span>Tallis Brook (Catholic)</li>
    <li><span class="check"></span>Plain of Wrens (Presbyterian)</li>
    <li><span class="check"></span>Pell Ridge</li>
    <li><span class="check"></span>Summary</li>
    <li><span class="check"></span>Quick Quiz</li>
  </ul>

  <ul class="utility">
    <li>Home</li><li>Help</li><li>Resources</li><li>Links</li>
  </ul>

  <nav class="topics">
    <div class="topic" style="left:0">
      <svg viewBox="0 0 50 48"><path d="M4 6 H22 Q25 6 25 10 V44 Q25 40 21 40 H4 Z M46 6 H28 Q25 6 25 10 V44 Q25 40 29 40 H46 Z" fill="#fff" stroke="#333" stroke-width="1.5"/><path d="M8 14 H21 M8 20 H21 M8 26 H21 M8 32 H21" stroke="#b3262b" stroke-width="2.5"/></svg>
      <span>History</span>
    </div>
    <div class="topic" style="left:126px">
      <svg viewBox="0 0 50 48"><rect x="8" y="2" width="34" height="40" fill="#e8e3d6"/><circle cx="22" cy="18" r="9" fill="none" stroke="#222" stroke-width="3"/><path d="M29 25 L40 38" stroke="#222" stroke-width="5"/></svg>
      <span>Map</span>
    </div>
    <div class="topic" style="left:255px">
      <svg viewBox="0 0 50 48"><path d="M4 16 Q25 2 46 16 L40 22 L34 16 H16 L10 22 Z" fill="#fff"/><path d="M12 24 H38 L42 42 H8 Z" fill="#fff"/><circle cx="25" cy="32" r="5" fill="#b3262b"/></svg>
      <span>Contact</span>
    </div>
    <div class="topic" style="left:383px">
      <svg viewBox="0 0 50 48"><rect x="23" y="2" width="4" height="46" fill="#fff"/><path d="M10 8 H38 L43 13 L38 18 H10 Z M40 22 H12 L7 27 L12 32 H40 Z" fill="#fff" stroke="#333" stroke-width="1.5"/></svg>
      <span>Directions</span>
    </div>
    <div class="topic" style="left:513px">
      <svg viewBox="0 0 50 48"><path d="M18 4 H22 V9 H26 V12 H22 V16 L28 24 H12 L18 16 Z M10 24 H30 V46 H10 Z M30 30 L44 26 V46 H30 Z" fill="#fff"/><rect x="17" y="34" width="6" height="12" fill="#b3262b"/></svg>
      <span>Services</span>
    </div>
    <div class="topic" style="left:644px">
      <svg viewBox="0 0 50 48"><path d="M20 2 H30 V14 H42 V24 H30 V48 H20 V24 H8 V14 H20 Z" fill="#fff"/></svg>
      <span>Sections</span>
    </div>
  </nav>

  <div class="module-mark"><span class="module-dot"></span><span class="module-name">DWT CEMETERIES MODULE</span></div>
  <div class="page-count">Page: 1 of 7</div>
</body>
</html>
```